New Business Card

We need to refresh our business cards. We designed these ourselves and we have no graphic design experience. We would like to find a new business card design that is professional and unique. We are an auto finance company. Feel free to play with the logo, but we would like to keep the eye very present on the card. Our corporate colors are green, grey, and white.
Green - RGB - 168,215,27; HEX - #AADD22
Grey - RGB - 196,196,196; HEX - #C4C4C4
Updates
Need to upload the vector file to finalize the project. The last logo was for a jpeg that didn't stretch well.
Industry/Entity Type
Financial Service
Contact Information for Business Card
Honestly don't know...I need your help!

```html
<!DOCTYPE html>
<html lang="en">
<head>
<meta charset="utf-8">
<title>Brightlane Capital – Business Card</title>
<link rel="stylesheet" href="https://fonts.googleapis.com/css2?family=Fira+Sans:wght@300;400;600&display=swap">
<style>
  :root {
    --green: #aadd22;
    --green-deep: #8cc21a;
    --grey: #c4c4c4;
    --charcoal: #3a3a3b;
    --ink: #555555;
    --paper: #ffffff;
    --backdrop: #e9e9e7;
  }
  * { box-sizing: border-box; margin: 0; padding: 0; }
  html, body { width: 1200px; height: 862px; overflow: hidden; }
  body {
    background: var(--backdrop);
    font-family: "Fira Sans", Arial, sans-serif;
    position: relative;
  }
  .card {
    position: absolute;
    width: 600px;
    height: 343px;
    border-radius: 3px;
    box-shadow: 0 8px 24px rgba(0,0,0,0.18);
  }
  .card--front {
    left: 90px; top: 70px;
    background: var(--charcoal);
  }
  .card--back {
    left: 510px; top: 450px;
    background: var(--paper);
  }
  .wordmark {
    display: flex;
    align-items: center;
    gap: 12px;
    color: var(--green);
    font-weight: 600;
    letter-spacing: 0.2px;
  }
  .wordmark__dot {
    width: 34px; height: 34px;
    border-radius: 50%;
    background: var(--green);
  }
  .card--front .wordmark {
    position: absolute;
    left: 0; right: 0; top: 120px;
    justify-content: center;
    font-size: 34px;
  }
  .card--front .website {
    position: absolute;
    left: 0; right: 0; top: 268px;
    text-align: center;
    color: #e5e5e5;
    font-size: 14px;
    font-weight: 300;
    letter-spacing: 0.3px;
  }
  .card--front .website span { color: var(--green); }

  .card--back .wordmark {
    position: absolute;
    right: 48px; top: 42px;
    font-size: 30px;
  }
  .card--back .wordmark__dot { width: 30px; height: 30px; }
  .rule {
    position: absolute;
    height: 1px;
    background: var(--grey);
  }
  .rule--top { left: 48px; right: 48px; top: 104px; }
  .address {
    position: absolute;
    right: 48px; top: 124px;
    text-align: right;
    font-size: 13px;
    font-weight: 300;
    line-height: 1.55;
    color: var(--ink);
  }
  .person {
    position: absolute;
    left: 48px; top: 168px;
  }
  .person__name {
    color: var(--green-deep);
    font-weight: 600;
    font-size: 21px;
    letter-spacing: 0.3px;
    text-transform: uppercase;
  }
  .person__title {
    margin-top: 4px;
    font-size: 13px;
    font-weight: 300;
    color: var(--ink);
  }
  .rule--name { left: 48px; width: 280px; top: 226px; }
  .contacts {
    position: absolute;
    left: 48px; top: 238px;
    list-style: none;
  }
  .contacts li {
    display: flex;
    align-items: center;
    gap: 10px;
    height: 22px;
    font-size: 13px;
    font-weight: 300;
    color: var(--ink);
  }
  .contacts svg { width: 13px; height: 13px; fill: var(--green-deep); }
</style>
</head>
<body>
  <section class="card card--front">
    <div class="wordmark"><span class="wordmark__dot"></span>Brightlane Capital</div>
    <p class="website">www.<span>brightlanecapital</span>.com</p>
  </section>

  <section class="card card--back">
    <div class="wordmark"><span class="wordmark__dot"></span>Brightlane Capital</div>
    <div class="rule rule--top"></div>
    <p class="address">Street Name Avenue, Suite<br>100 State, Zip Code,Country</p>

    <div class="person">
      <h1 class="person__name">Daniel R. Moore</h1>
      <p class="person__title">Resident Manager</p>
    </div>
    <div class="rule rule--name"></div>

    <ul class="contacts">
      <li>
        <svg viewBox="0 0 16 16" aria-hidden="true"><path d="M3.5 1l2.5 3-1.5 2c1 2 3 4 5 5l2-1.5 3 2.5-1.5 2.5C7 16 0 9 1 2.5z"/></svg>
        555-214-3870
      </li>
      <li>
        <svg viewBox="0 0 16 16" aria-hidden="true"><path d="M3 6l1.5-3.5h7L13 6h1v5h-1.5v2h-2v-2h-5v2h-2v-2H2V6zM4.5 6h7l-1-2h-5zM4 8a1 1 0 1 0 0 .01zM12 8a1 1 0 1 0 0 .01z"/></svg>
        555-386-1042
      </li>
      <li>
        <svg viewBox="0 0 16 16" aria-hidden="true"><path d="M1 3h14v10H1zM2.5 4.5v.3L8 9l5.5-4.2v-.3zM2.5 6.6v5h11v-5L8 10.8z"/></svg>
        info@brightlanecapital.com
      </li>
      <li>
        <svg viewBox="0 0 16 16" aria-hidden="true"><circle cx="8" cy="8" r="7"/><path d="M1 8h14M8 1c-3 3-3 11 0 14M8 1c3 3 3 11 0 14" stroke="#fff" stroke-width="1" fill="none"/></svg>
        www.brightlanecapital.com
      </li>
    </ul>
  </section>
</body>
</html>
```